Website Landing Page for Brightfall Systems

Create a custom designed website landing page for our business. Looking for a professional upscale design that incorporates our logo and logo colors into the theme. I want a standard fixed frame website, not a constant scrolling format that seems to be the trend. To start with I'm looking for more of the graphic design part, maybe a concept or theme, I don't expect to see a finished project. Not interested in generic templates or layouts.

The name of our company is Brightfall Systems and I've attached our logo below. I'd like to have the web page have the same look and feel of our logo, as well as the colors. Our company, Brightfall Systems does system design, installation, and programming, of residential and commercial Audio/Video and Automation systems. We do home theaters, lighting and building automation, video conferencing systems, security camera installations, conference rooms, projectors, distributed audio systems, and similar Technology projects. This will be a professional services/informational website. We will not sell products on this website. This website will be used to advertise our company and communicate our services to prospective customers. Having a well designed, professional and clean website is one way we want to distinguish our company from the competition.

Here are some examples of what I consider a professional well designed website
http://www.qorlamstudio.com/Work/

Last year we had our tradlo store designed (with PixelMarket) and I'm really happy with the way it turned out. You can see it at www.HolvenGearDepot.com I consider this to be a great design and looking for the same level of quality with this new website. However, do not copy or use any part of this design in this new project. This tradlo store is completely separate from our other company Brightfall Systems. I only mention this tradlo store an an example of good work.

Reason: Still going through designs.

Reason: Still working on project and have not had time to review all designs and request revisions.

Reason: Sill going through designs and requesting revisions

Reason: still going through all the submissions we received.

Target Market(s)

People interested in Audio/Video, home theaters, home automation. We do sales, system design, and programming. We typically work on larger projects with both residential and commercial customers.

Industry/Entity Type

Business

Number of Pages Required

1 page

Requirements
Must have
• Great design elements. Please use a white background. I think white goes well with our logo colors.

```html
<!DOCTYPE html>
<html lang="en">
<head>
<meta charset="utf-8">
<title>Brightfall Systems</title>
<link href="https://fonts.googleapis.com/css2?family=Hind:wght@300;400;500;600&family=Open+Sans:wght@400;600;700&display=swap" rel="stylesheet">
<style>
  :root {
    --blue: #4a90e2;
    --blue-dark: #3d7fd0;
    --ink: #333a44;
    --muted: #6b7078;
    --line: #e5e7ea;
    --soft: #f3f3f3;
    --footer: #25262e;
    --white: #ffffff;
    --brand-green: #3fae49;
  }
  * { box-sizing: border-box; margin: 0; padding: 0; }
  html, body { width: 909px; height: 1200px; overflow: hidden; background: var(--white); }
  body { position: relative; font-family: "Open Sans", sans-serif; color: var(--ink); }
  .abs { position: absolute; }

  .top-bar { left: 0; top: 0; width: 909px; height: 37px; border-bottom: 1px solid var(--line); background: #fafafa; }
  .top-bar .email { left: 80px; top: 13px; font-size: 8px; letter-spacing: .6px; color: var(--muted); text-transform: uppercase; }
  .top-bar .social { right: 80px; top: 12px; display: flex; gap: 17px; }
  .top-bar .social span { width: 12px; height: 12px; border-radius: 50%; background: #b8bcc2; display: block; }

  .nav-bar { left: 0; top: 37px; width: 909px; height: 61px; }
  .brand { left: 80px; top: 10px; display: flex; align-items: center; gap: 9px; }
  .brand .dot { width: 42px; height: 42px; border-radius: 50%; border: 4px solid var(--blue); }
  .brand .name { font-family: "Hind", sans-serif; font-weight: 600; font-size: 13px; line-height: 13px; color: var(--brand-green); letter-spacing: .5px; text-transform: uppercase; }
  .menu { right: 81px; top: 27px; display: flex; gap: 20px; font-size: 8.6px; letter-spacing: .6px; color: #555; text-transform: uppercase; }

  .hero { left: 0; top: 98px; width: 909px; height: 374px;
    background: linear-gradient(100deg, #3e444c 0%, #6a6f75 30%, #8a8c8e 55%, #6f5a48 75%, #4d3e33 100%); }
  .hero-title { left: 80px; top: 85px; width: 420px; font-family: "Hind", sans-serif; font-weight: 400; font-size: 32px; line-height: 37px; color: var(--white); letter-spacing: -.4px; }
  .hero-sub { left: 80px; top: 205px; width: 440px; font-size: 10.4px; line-height: 18px; color: #eef0f2; letter-spacing: .3px; }
  .btn { background: var(--blue); color: var(--white); font-size: 8.6px; letter-spacing: .8px; text-transform: uppercase; display: flex; align-items: center; justify-content: center; }
  .hero-btn { left: 80px; top: 251px; width: 97px; height: 31px; }

  .enquiry { left: 528px; top: 123px; width: 301px; height: 275px; background: var(--white); box-shadow: 0 2px 10px rgba(0,0,0,.15); }
  .enquiry h3 { position: absolute; left: 21px; top: 42px; font-family: "Hind", sans-serif; font-weight: 400; font-size: 13.5px; letter-spacing: .2px; color: var(--ink); }
  .field { position: absolute; left: 21px; width: 260px; height: 30px; border: 1px solid #dcdfe3; font-size: 9px; color: #b2b6bb; padding: 9px 8px; }
  .enquiry .btn { position: absolute; left: 21px; top: 200px; width: 101px; height: 30px; font-size: 8px; letter-spacing: .2px; }
  .enquiry .note { position: absolute; left: 21px; top: 243px; font-size: 8px; letter-spacing: .6px; color: var(--muted); text-transform: uppercase; }

  .section-title { left: 0; width: 909px; text-align: center; font-family: "Hind", sans-serif; font-weight: 400; font-size: 16.5px; color: var(--ink); text-transform: uppercase; }
  .expertise-intro { left: 80px; top: 545px; width: 749px; text-align: center; font-size: 10px; line-height: 18px; color: var(--muted); letter-spacing: .3px; }

  .card { top: 607px; width: 242px; height: 154px; background: var(--blue); border: 1px solid var(--blue-dark); color: var(--white); padding: 30px 16px 0; }
  .card h4 { font-family: "Hind", sans-serif; font-weight: 400; font-size: 11.5px; text-transform: uppercase; letter-spacing: -.1px; margin-bottom: 3px; }
  .card p { font-size: 9.3px; line-height: 17px; color: #dbe8f8; letter-spacing: .3px; }
  .card .more { margin-top: 10px; font-size: 8.6px; font-weight: 700; letter-spacing: .7px; text-transform: uppercase; }

  .dots { left: 438px; top: 790px; display: flex; gap: 7px; }
  .dots span { width: 7px; height: 7px; border-radius: 50%; background: #c4c6c9; display: block; }
  .dots span.on { background: #222; }

  .scroll-tab { left: 835px; top: 809px; width: 42px; height: 18px; border-radius: 21px 21px 0 0; background: var(--white); box-shadow: 0 -2px 4px rgba(0,0,0,.06); }

  .partners { left: 0; top: 887px; width: 909px; height: 133px; background: var(--soft); }
  .partner { position: absolute; top: 23px; width: 153px; height: 88px; background: var(--white); border: 1px solid #e3e4e6; display: flex; align-items: center; justify-content: center; }
  .badge-rect { width: 100px; height: 22px; background: #c9ccd1; border-radius: 3px; }
  .badge-circle { width: 40px; height: 40px; background: #ecd27a; border-radius: 50%; }

  .footer { left: 0; top: 1020px; width: 909px; height: 180px; background: var(--footer); }
  .footer .brand { left: 365px; top: 22px; gap: 12px; }
  .footer .brand .dot { width: 62px; height: 62px; border-width: 5px; }
  .footer .brand .name { font-size: 19px; line-height: 19px; }
  .footer-social { left: 362px; top: 110px; display: flex; gap: 4px; }
  .footer-social span { width: 27px; height: 27px; background: var(--blue); display: block; }
  .copyright { left: 0; top: 148px; width: 909px; text-align: center; font-family: "Hind", sans-serif; font-size: 11px; color: #d9dadd; }
  .to-top { left: 856px; top: 1170px; width: 23px; height: 23px; border-radius: 3px; background: #1a9af0; }
</style>
</head>
<body>

<header class="abs top-bar">
  <div class="abs email">Email: support@brightfallsystems.com</div>
  <div class="abs social"><span></span><span></span><span></span><span></span><span></span></div>
</header>

<nav class="abs nav-bar">
  <div class="abs brand">
    <div class="dot"></div>
    <div class="name">Brightfall<br>Systems</div>
  </div>
  <div class="abs menu">
    <span>Home</span><span>About</span><span>Service</span><span>Video</span><span>Reviews</span><span>Blog</span><span>Contact</span>
  </div>
</nav>

<section class="abs hero" role="img" aria-label="Photo of a person working at a laptop on a wooden desk">
  <h1 class="abs hero-title">For Best Residential and Commercial Automation System.</h1>
  <p class="abs hero-sub">We do home theaters, lighting and building automation, video conferencing systems, security camera installations.</p>
  <div class="abs btn hero-btn">Learn More</div>
</section>

<form class="abs enquiry">
  <h3>QUICK CONTACT FOR ENQUIRY!</h3>
  <div class="field" style="top:79px">Enter your full name</div>
  <div class="field" style="top:119px">Enter your email</div>
  <div class="field" style="top:159px">Phone No.</div>
  <div class="btn">CONTACT NOW!</div>
  <p class="note">We never share your details with anyone.</p>
</form>

<h2 class="abs section-title" style="top:514px">Our Area of Expertise!</h2>
<p class="abs expertise-intro">We do home theaters, lighting and building automation, video conferencing systems, security camera installations, conference rooms, projectors, distributed audio systems, and similar Technology projects.</p>

<article class="abs card" style="left:71px">
  <h4>Title Goes Here</h4>
  <p>Lorem ipsum dolor sit amet, consectetur adipiscing elit, sed do eiusmod tempor incididunt ut labore et dolore magna aliqua.</p>
  <div class="more">Learn More</div>
</article>
<article class="abs card" style="left:334px">
  <h4>Title Goes Here</h4>
  <p>Lorem ipsum dolor sit amet, consectetur adipiscing elit, sed do eiusmod tempor incididunt ut labore et dolore magna aliqua.</p>
  <div class="more">Learn More</div>
</article>
<article class="abs card" style="left:597px">
  <h4>Title Goes Here</h4>
  <p>Lorem ipsum dolor sit amet, consectetur adipiscing elit, sed do eiusmod tempor incididunt ut labore et dolore magna aliqua.</p>
  <div class="more">Learn More</div>
</article>

<div class="abs dots"><span class="on"></span><span></span><span></span></div>
<div class="abs scroll-tab">
  <svg width="42" height="18" viewBox="0 0 42 18"><path d="M18.5 12 L21 9.5 L23.5 12" fill="none" stroke="#555" stroke-width="1"/></svg>
</div>

<h2 class="abs section-title" style="top:850px">Our Partners</h2>
<section class="abs partners">
  <div class="partner" style="left:96px"><div class="badge-rect"></div></div>
  <div class="partner" style="left:288px"><div class="badge-circle"></div></div>
  <div class="partner" style="left:480px"><div class="badge-rect"></div></div>
  <div class="partner" style="left:672px"><div class="badge-circle"></div></div>
</section>

<footer class="abs footer">
  <div class="abs brand">
    <div class="dot"></div>
    <div class="name">Brightfall<br>Systems</div>
  </div>
  <div class="abs footer-social"><span></span><span></span><span></span><span></span><span></span><span></span></div>
  <p class="abs copyright">Copyright © 2017 Brightfall Systems | All Rights Reserved</p>
</footer>

<div class="abs to-top">
  <svg width="23" height="23" viewBox="0 0 23 23"><path d="M8 13.5 L11.5 10 L15 13.5" fill="none" stroke="#fff" stroke-width="1.6"/></svg>
</div>

</body>
</html>
```